Hot Dog Menu 1

Web, TV, and print menu design project by 1) digitize or draw from a hand drawn menu, 2) make it available in 18 x 48 (in) for a print, 3) make it available to 1920 x 1080 (px) for a TV / USB, 3) make it available in two brand (logo provided). Attached files description: DNHD menu is the one we drew, Menu1 is the menu used by one of our competitor which we like ours to be like. Logo (Tolsa Tolsa) is the second brand we are about to launch. Dalnim Hot Dog logo, you already have that from the previous project. The project is to create two identical menu board, one for Dalnim and the other one is for Tolsa Tolsa to be displayed on TV (via USB), and to be printed on 18 x 48 prints. If you are interested to work on this project, please let me know.

```html
<!DOCTYPE html>
<html lang="en">
<head>
<meta charset="utf-8">
<title>Hot Dog Menu</title>
<link rel="stylesheet" href="https://fonts.googleapis.com/css2?family=Exo+2:wght@700;800&display=swap">
<style>
  :root {
    --page-bg: #ececec;
    --board-dark: #141414;
    --board-mid: #2a2a2a;
    --board-edge: #050505;
    --text-light: #ffffff;
    --grill-light: #e49a5a;
    --grill-dark: #a9502a;
    --smoked-light: #9a5a34;
    --smoked-dark: #4a2110;
    --ricecake-light: #c8642e;
    --ricecake-dark: #5e1a0c;
    --ham-light: #f1c6c4;
    --ham-dark: #b86a4a;
  }
  * { margin: 0; padding: 0; box-sizing: border-box; }
  html, body {
    width: 1200px;
    height: 600px;
    overflow: hidden;
    background: var(--page-bg);
  }
  .menu-board {
    position: absolute;
    left: 0;
    top: 75px;
    width: 1200px;
    height: 450px;
    background:
      radial-gradient(ellipse at 30% 20%, rgba(80,80,80,0.35), transparent 55%),
      radial-gradient(ellipse at 70% 75%, rgba(70,70,70,0.3), transparent 60%),
      radial-gradient(ellipse at 55% 45%, var(--board-mid), var(--board-dark) 80%);
    border-right: 6px solid var(--board-edge);
    font-family: "Exo 2", sans-serif;
    color: var(--text-light);
  }
  .menu-title {
    position: absolute;
    top: 38px;
    left: 0;
    width: 100%;
    text-align: center;
    font-size: 60px;
    font-weight: 800;
    letter-spacing: -1px;
    line-height: 1;
  }
  .item-photo {
    position: absolute;
    border-radius: 40%;
  }
  .item-photo.grilled {
    background: radial-gradient(ellipse at 50% 40%, var(--grill-light), var(--grill-dark) 75%, transparent 76%);
  }
  .item-photo.smoked {
    background: radial-gradient(ellipse at 50% 50%, var(--smoked-light), var(--smoked-dark) 72%, transparent 73%);
  }
  .item-photo.curly {
    background: radial-gradient(ellipse at 50% 50%, var(--grill-light), var(--grill-dark) 72%, transparent 73%);
  }
  .item-photo.ricecake {
    background: radial-gradient(ellipse at 50% 50%, var(--ricecake-light), var(--ricecake-dark) 72%, transparent 73%);
  }
  .item-photo.sliced {
    background: radial-gradient(ellipse at 55% 55%, var(--ham-light), var(--ham-dark) 72%, transparent 73%);
  }
  .item-name {
    position: absolute;
    font-size: 11px;
    font-weight: 700;
    white-space: nowrap;
    line-height: 14px;
  }
</style>
</head>
<body>
  <main class="menu-board">
    <h1 class="menu-title">HOT DOG MENU</h1>

    <div class="item-photo grilled" style="left:112px;top:121px;width:115px;height:75px" role="img" aria-label="Grilled pork and beef sausages"></div>
    <p class="item-name" style="left:264px;top:170px">PORK AND BEEF SAUSAGE</p>

    <div class="item-photo grilled" style="left:112px;top:218px;width:115px;height:76px" role="img" aria-label="Grilled beef sausages"></div>
    <p class="item-name" style="left:264px;top:276px">BEEF SAUSAGE</p>

    <div class="item-photo ricecake" style="left:112px;top:326px;width:115px;height:59px" role="img" aria-label="Glazed rice cake skewer"></div>
    <p class="item-name" style="left:264px;top:346px">RICE CAKE</p>

    <div class="item-photo smoked" style="left:459px;top:134px;width:137px;height:50px" role="img" aria-label="Thin smoked pork and beef mozzarella sausages"></div>
    <p class="item-name" style="left:618px;top:166px">PORK AND BEEF&nbsp; MOZZARILA SAUSAGE</p>

    <div class="item-photo curly" style="left:459px;top:238px;width:137px;height:51px" role="img" aria-label="Curved beef sausages with potatoes"></div>
    <p class="item-name" style="left:614px;top:276px">BEEF SAUSAGE POTATOES</p>

    <div class="item-photo sliced" style="left:459px;top:338px;width:106px;height:61px" role="img" aria-label="Sliced mozzarella sausage"></div>
    <p class="item-name" style="left:621px;top:366px">MOZZARILA</p>

    <div class="item-photo grilled" style="left:850px;top:118px;width:116px;height:76px" role="img" aria-label="Grilled cheddar pork and beef sausages"></div>
    <p class="item-name" style="left:988px;top:174px">CHEDDAR PORK AND BEEF&nbsp; SAUSAGE</p>

    <div class="item-photo grilled" style="left:850px;top:231px;width:116px;height:74px" role="img" aria-label="Grilled mozzarella pork and beef sausages"></div>
    <p class="item-name" style="left:988px;top:289px">MOZZARILA PORK AND BEEF SAUSAGE</p>

    <div class="item-photo sliced" style="left:850px;top:349px;width:108px;height:61px" role="img" aria-label="Sliced mozzarella cheddar sausage"></div>
    <p class="item-name" style="left:988px;top:371px">MOZZARILA CHEDDAR</p>
  </main>
</body>
</html>
```